Poster for our end of year annual dance concert

We need an A3 portrait poster for our end of year concert.
Designs are attached of posters from previous 3 years as a reference only.
The theme of our concert this year is "Comets & Lanterns ".
This is a fun them with dance routines choreographed to songs such as "Glimmerlass", "Fox Maiden", "Zip Lassie", "Quillor", "The Tinker", "Velvet Otters", "Drifters", "Gremlets", etc, etc
Dance styles in the concert include Jazz & Hip Hop.
Bright colors are preferred in the design.

Target Market(s)

Dance school students & their families

Industry/Entity Type

Dance Studio

Font styles to use
Sans Serif

Requirements
Must have
• Size: A3 Portrait
• You will see in the samples from previous years the poster must have:
• The Rosalind Pike Dancers (font is Mistral) + logo (supplied)
• Bellward Theatre
• Marlowe College Fernbrook
• Concert date this year is: Saturday 19th November
• Website: www.rpkdancers-site.com.au
Nice to have
• Clean design, not cluttered with too much imagery

```html
<!DOCTYPE html>
<html lang="en">
<head>
<meta charset="utf-8">
<title>Comets &amp; Lanterns — The Rosalind Pike Dancers</title>
<link rel="stylesheet" href="https://fonts.googleapis.com/css2?family=Antonio:wght@300&family=Dancing+Script:wght@500&family=Fira+Sans:wght@700&family=Open+Sans:wght@300&family=Raleway:wght@300&display=swap">
<style>
  :root {
    --paper: #ffffff;
    --sand-light: #d9c3a0;
    --sand: #c8a47a;
    --amber: #c98a4e;
    --rust: #b8703a;
    --flame-yellow: #ffe43a;
    --flame-orange: #ff8a1c;
    --flame-red: #f04a12;
    --cream: #fffbe8;
    --ink: #2a1d12;
  }
  html, body {
    margin: 0;
    padding: 0;
    width: 849px;
    height: 1200px;
    overflow: hidden;
    background: var(--paper);
  }
  .poster {
    position: relative;
    width: 849px;
    height: 1200px;
    background: var(--paper);
  }
  .poster__field {
    position: absolute;
    left: 14px;
    top: 14px;
    width: 821px;
    height: 1172px;
    overflow: hidden;
    background:
      repeating-linear-gradient(90deg, rgba(255,255,255,0.06) 0 14px, rgba(120,70,30,0.05) 14px 31px, rgba(255,255,255,0.04) 31px 52px),
      linear-gradient(90deg, var(--sand-light) 0%, #d6b790 25%, var(--sand) 50%, #d2a674 72%, var(--amber) 88%, var(--rust) 100%);
  }
  .dancer {
    position: absolute;
    top: 270px;
    width: 170px;
    height: 760px;
    border-radius: 40% 40% 35% 35%;
    filter: blur(22px);
  }
  .dancer--hero {
    left: 165px;
    background: linear-gradient(180deg, rgba(255,180,60,0.5) 0%, rgba(255,200,40,0.85) 35%, var(--flame-yellow) 60%, rgba(255,140,30,0.8) 85%, rgba(255,120,20,0.3) 100%);
  }
  .dancer--villain {
    left: 485px;
    background: linear-gradient(180deg, rgba(240,150,70,0.45) 0%, rgba(255,150,40,0.8) 35%, var(--flame-orange) 60%, var(--flame-red) 88%, rgba(240,80,20,0.3) 100%);
  }
  .brand {
    position: absolute;
    top: 44px;
    left: 0;
    width: 100%;
    display: flex;
    justify-content: center;
    align-items: center;
    gap: 8px;
  }
  .brand__name {
    font-family: "Fira Sans", sans-serif;
    font-weight: 700;
    font-size: 30px;
    color: var(--ink);
  }
  .brand__dot {
    width: 12px;
    height: 12px;
    border-radius: 50%;
    background: var(--ink);
  }
  .company {
    position: absolute;
    top: 138px;
    width: 100%;
    text-align: center;
    font-family: "Dancing Script", cursive;
    font-weight: 500;
    font-size: 50px;
    color: var(--cream);
    text-shadow: 1px 2px 2px rgba(60,30,10,0.55);
  }
  .presents {
    position: absolute;
    top: 230px;
    width: 100%;
    text-align: center;
    font-family: "Raleway", sans-serif;
    font-weight: 300;
    font-size: 38px;
    letter-spacing: 0.55em;
    text-indent: 0.55em;
    color: var(--paper);
  }
  .title {
    position: absolute;
    top: 462px;
    left: 50%;
    width: max-content;
    margin: 0;
    white-space: nowrap;
    transform: translateX(-50%) scaleX(0.7);
    transform-origin: center;
    font-family: "Antonio", sans-serif;
    font-weight: 300;
    font-size: 150px;
    line-height: 1;
    color: var(--cream);
    background: linear-gradient(90deg, #ffffff 0%, #fff6b0 22%, var(--flame-yellow) 40%, #ffffff 55%, var(--flame-yellow) 72%, #ffffff 100%);
    -webkit-background-clip: text;
    background-clip: text;
    -webkit-text-fill-color: transparent;
    filter: drop-shadow(2px 3px 2px rgba(70,40,15,0.55));
  }
  .date {
    position: absolute;
    top: 668px;
    width: 100%;
    text-align: center;
    font-family: "Open Sans", sans-serif;
    font-weight: 300;
    font-size: 62px;
    color: var(--cream);
    text-shadow: 1px 2px 2px rgba(110,50,10,0.45);
  }
  .venue {
    position: absolute;
    left: 44px;
    top: 985px;
    font-family: "Fira Sans", sans-serif;
    font-weight: 700;
    font-size: 27px;
    color: var(--paper);
    line-height: 1;
  }
  .venue p { margin: 0 0 26px; }
  .venue .website { margin-top: 36px; }
</style>
</head>
<body>
  <main class="poster">
    <section class="poster__field">
      <div class="dancer dancer--hero" role="img" aria-label="Blurred dancer silhouette glowing in yellow flame tones"></div>
      <div class="dancer dancer--villain" role="img" aria-label="Blurred dancer silhouette glowing in orange and red flame tones"></div>

      <div class="brand">
        <span class="brand__dot"></span>
        <span class="brand__name">RPD</span>
      </div>

      <div class="company">The Rosalind Pike Dancers</div>
      <div class="presents">PRESENTS</div>

      <h1 class="title">COMETS &amp; LANTERNS</h1>

      <div class="date">Saturday 19th November</div>

      <div class="venue">
        <p>Bellward Theatre</p>
        <p>Marlowe College Fernbrook</p>
        <p class="website">www.rpkdancers-site.com.au</p>
      </div>
    </section>
  </main>
</body>
</html>
```